New PowerPoint Design Project

This is another powerpoint project for our scholarship fund.

I want a refresh on the look of the slide deck. Attached is last year's slide deck so you can see the type of information that is shared plus the logo.

Thank you.

```html
<!DOCTYPE html>
<html lang="en">
<head>
<meta charset="utf-8">
<title>HVMEF 2020 Central Regional Conference – Slide Deck</title>
<link href="https://fonts.googleapis.com/css2?family=Lato:wght@300;400;700;900&family=Open+Sans:wght@400;600;700&display=swap" rel="stylesheet">
<style>
:root{
  --canvas:#e0e3f5;
  --paper:#f3f3f3;
  --blue:#1a8fcf;
  --blue-deep:#1878bc;
  --heading:#1c7cc0;
  --red:#e2203c;
  --pink:#e51c7b;
  --pink-band:rgba(229,28,123,.9);
  --violet-band:rgba(240,120,225,.88);
  --teal-band:rgba(82,186,156,.9);
  --coral-band:rgba(240,78,80,.9);
  --blue-band:rgba(26,143,207,.9);
  --ink:#333;
  --muted:#555;
  --white:#fff;
}
*{box-sizing:border-box;margin:0;padding:0}
html,body{width:1200px;height:3000px;overflow:hidden}
body{background:var(--canvas);font-family:"Lato",sans-serif;color:var(--ink);position:relative}
.slide{position:absolute;width:487px;height:275px;background:var(--paper);box-shadow:0 6px 16px rgba(40,40,80,.28);overflow:hidden}
.col-l{left:91px}.col-r{left:619px}
.mark{position:absolute;right:10px;bottom:8px;width:8px;height:8px;background:var(--blue)}
.photo-team{position:absolute;inset:0;background:linear-gradient(180deg,#e4e8ea 0%,#c9c4b2 22%,#8d7a5d 45%,#5b4a3a 62%,#a7783f 82%,#c9914d 100%)}
.band{position:absolute;left:11px;right:11px;color:var(--white);font-family:"Lato",sans-serif;font-weight:400}
.section .band{top:182px;height:82px;padding:0 24px;display:flex;align-items:center;font-size:18px;line-height:1.2}
.band.pink{background:var(--pink-band)}.band.violet{background:var(--violet-band)}.band.teal{background:var(--teal-band)}.band.coral{background:var(--coral-band)}.band.blue{background:var(--blue-band)}
.brand-tag{position:absolute;left:38px;top:158px;background:var(--white);padding:3px 6px;display:flex;align-items:center;gap:4px;font-family:"Lato",sans-serif;font-weight:700;font-size:10px;color:var(--blue-deep)}
.brand-tag i{width:7px;height:7px;background:var(--blue)}
.cover .band{top:137px;height:128px;padding:14px 26px}
.cover .fund-name{font-size:7px;letter-spacing:3px;font-weight:700}
.cover h1{font-size:31px;font-weight:900;letter-spacing:2px;margin-top:12px;line-height:1}
.cover h2{font-size:26px;font-weight:700;letter-spacing:1.5px;margin-top:10px}
.cover .brand-tag{left:auto;right:24px;top:14px;position:absolute}
.agenda .snow{position:absolute;left:0;top:0;bottom:0;width:107px;background:linear-gradient(180deg,#dfe6ee,#c4d3e2 60%,#e9edf1)}
.agenda h3{position:absolute;left:120px;top:58px;font-size:36px;font-weight:700;color:var(--blue)}
.agenda ul{position:absolute;left:120px;top:120px;width:318px;list-style:none}
.agenda li{display:flex;align-items:center;gap:6px;font-size:6.2px;font-weight:700;color:#444;height:18px;border-bottom:1px solid #9bc8e4}
.agenda li b{width:12px;height:12px;border-radius:50%;flex:none}
.s-head{position:absolute;left:34px;top:22px;color:var(--heading);font-family:"Open Sans",sans-serif;font-weight:700}
.s-head .t{font-size:16px}.s-head .st{font-size:13px;margin-top:2px}
.chart{position:absolute}
.survey{background:var(--blue)}
.survey .frame{position:absolute;inset:6px;border:2px solid var(--white);border-right:none;border-bottom:none}
.survey h3{position:absolute;left:34px;top:30px;color:var(--white);font-family:"Open Sans",sans-serif;font-size:16px;font-weight:700}
.survey .rule{position:absolute;left:34px;right:30px;top:56px;height:1px;background:rgba(255,255,255,.6)}
.survey ol{position:absolute;left:40px;top:66px;width:360px;color:var(--white);font-size:7.5px;list-style:none}
.survey ol>li{margin-bottom:16px}
.survey ol>li::before{content:"•";margin-right:8px}
.survey ul{list-style:none;margin:4px 0 0 32px;line-height:1.6}
.survey .q{position:absolute;right:28px;bottom:22px;font-size:140px;font-weight:900;color:#4bb8ec;line-height:1}
.covers{position:absolute;left:34px;top:76px;width:224px;height:175px;background:#ece7ef}
.covers .img{position:absolute;left:10px;top:8px;right:10px;height:118px;background:linear-gradient(135deg,#d7cfe0,#9a8aa8 45%,#3a3344 75%,#c7b9cc)}
.covers p{position:absolute;left:8px;right:8px;top:131px;text-align:center;font-size:7px;line-height:1.3;color:#333}
.covers small{position:absolute;left:8px;right:8px;top:157px;text-align:center;font-size:4.5px;color:var(--blue)}
.stats{position:absolute;left:282px;top:86px;width:165px;text-align:center}
.stats div{padding:8px 0 7px;border-bottom:1px solid #9bc8e4;font-size:9px}
.stats div:last-child{border:none}
.stats strong{display:block;font-size:13px;font-weight:400;color:#222;margin-bottom:5px}
.stats strong em{font-style:normal;font-weight:900;color:var(--red);font-size:17px}
.mission .img{position:absolute;left:0;top:0;bottom:0;width:198px;background:linear-gradient(180deg,#6c6a63,#3c3d3a 45%,#8a7c60 75%,#5f5a4f)}
.mission h3{position:absolute;left:224px;top:38px;font-family:"Open Sans",sans-serif;font-weight:700;font-size:16px;color:var(--heading);line-height:1.35}
.mission p{position:absolute;left:224px;top:104px;width:225px;font-size:8.4px;line-height:1.95;color:var(--muted);font-weight:400}
.facts .img{position:absolute;right:0;top:0;bottom:0;width:197px;background:linear-gradient(180deg,#3d4854,#6c7480 40%,#9aa0a6 70%,#c9cacc)}
.facts ul{position:absolute;left:34px;top:72px;width:240px;list-style:none;font-size:8.2px;line-height:1.95;color:var(--muted);font-weight:400}
.facts li{padding-left:12px;position:relative}
.facts li::before{content:"✓";position:absolute;left:0;color:var(--muted)}
.facts li.sub{padding-left:30px}
.facts li.sub::before{content:"•";left:20px}
.bstr h3{position:absolute;left:27px;top:18px;font-family:"Open Sans",sans-serif;font-weight:700;font-size:15px;color:var(--heading)}
.bstr h4{position:absolute;left:27px;top:38px;font-size:11px;font-weight:400;color:var(--blue)}
.bstr ul{position:absolute;left:38px;top:56px;width:430px;font-size:6.7px;line-height:1.42;color:#333}
.bstr .img{position:absolute;left:0;right:0;bottom:0;height:107px;background:linear-gradient(180deg,#3a2a22,#7a5138 45%,#c08a52 60%,#2e2420)}
.natl h3{position:absolute;left:48px;top:40px;font-family:"Open Sans",sans-serif;font-weight:700;font-size:14px;color:var(--heading)}
.natl .card{position:absolute;left:45px;top:64px;width:397px;height:150px;background:var(--blue-deep);border-radius:8px;color:var(--white)}
.natl .card .img{position:absolute;left:18px;top:14px;width:108px;height:122px;background:linear-gradient(180deg,#cfc9c3,#8a6f63 55%,#2c2322)}
.natl .card .rule{position:absolute;left:142px;top:14px;width:1px;height:122px;background:rgba(255,255,255,.6)}
.natl .card h4{position:absolute;left:157px;top:14px;font-size:12px;font-weight:700;line-height:1.4}
.natl .card ul{position:absolute;left:160px;top:66px;width:220px;font-size:8px;line-height:1.5;padding-left:10px}
.thanks h3{position:absolute;left:0;right:0;top:24px;text-align:center;font-family:"Open Sans",sans-serif;font-weight:700;font-size:14px;letter-spacing:2px;color:var(--blue);line-height:1.35}
.person{position:absolute;top:80px;width:130px;text-align:center}
.person .img{position:relative;height:103px;background:linear-gradient(180deg,#d9dbdc,#b79a86 55%,#4a4a55)}
.person .img::before{content:"";position:absolute;left:-5px;top:-5px;width:22px;height:22px;border-left:5px solid var(--blue);border-top:5px solid var(--blue)}
.person .nm{font-size:6.5px;letter-spacing:2px;margin-top:12px;color:#555}
.person .rl{font-size:6px;margin-top:4px;color:#555}
.thanks .footbar{position:absolute;left:0;right:0;bottom:0;height:12px;background:var(--blue)}
</style>
</head>
<body>

<section class="slide cover col-l" style="top:59px">
  <div class="photo-team" role="img" aria-label="Photo of a smiling group of young women standing outdoors"></div>
  <div class="band blue">
    <p class="fund-name">Harriet Vale Memorial Education Fund (HVMEF)</p>
    <h1>2020</h1>
    <h2>Central Regional Conference</h2>
    <div class="brand-tag"><i></i>HVMEF</div>
  </div>
</section>

<section class="slide agenda col-r" style="top:59px">
  <div class="snow" role="img" aria-label="Photo of footprints in snow"></div>
  <h3>Agenda</h3>
  <ul>
    <li><b style="background:#1a8fcf"></b>Mission, Facts, and Contributions by District and the Business Case for HVMEF in 2020</li>
    <li><b style="background:#f04e50"></b>HVMEF Resources and Where to Find Them</li>
    <li><b style="background:#e51c7b"></b>Responsibilities of Trustees</li>
    <li><b style="background:#c8177a"></b>Ways You can Support HVMEF</li>
    <li><b style="background:#52ba9c"></b>General Policies for Administering HVMEF</li>
    <li><b style="background:#f29be8"></b>HVMEF Scholarship Programs for 2020-2021</li>
  </ul>
  <span class="mark"></span>
</section>

<section class="slide section col-l" style="top:386px">
  <div class="photo-team" role="img" aria-label="Photo of a smiling group of young women standing outdoors"></div>
  <div class="brand-tag"><i></i>HVMEF</div>
  <div class="band violet">HVMEF Scholarship Programs for 2020-2021 and Eligibility Requirements for Leagues and Applicants</div>
</section>

<section class="slide section col-r" style="top:386px">
  <div class="photo-team" role="img" aria-label="Photo of a smiling group of young women standing outdoors"></div>
  <div class="brand-tag"><i></i>HVMEF</div>
  <div class="band teal">General Policies For Administering HVMEF</div>
</section>

<section class="slide section col-l" style="top:713px">
  <div class="photo-team" role="img" aria-label="Photo of a smiling group of young women standing outdoors"></div>
  <div class="brand-tag"><i></i>HVMEF</div>
  <div class="band pink">Ways You Can Support HVMEF</div>
</section>

<section class="slide section col-r" style="top:713px">
  <div class="photo-team" role="img" aria-label="Photo of a smiling group of young women standing outdoors"></div>
  <div class="brand-tag"><i></i>HVMEF</div>
  <div class="band pink">Responsibilities of HVMEF Trustee</div>
</section>

<section class="slide section col-l" style="top:1039px">
  <div class="photo-team" role="img" aria-label="Photo of a smiling group of young women standing outdoors"></div>
  <div class="brand-tag"><i></i>HVMEF</div>
  <div class="band blue">Mission, Facts, Contributions by District and the Business Case for HVMEF in 2020</div>
</section>

<section class="slide section col-r" style="top:1039px">
  <div class="photo-team" role="img" aria-label="Photo of a smiling group of young women standing outdoors"></div>
  <div class="brand-tag"><i></i>HVMEF</div>
  <div class="band coral">HVMEF Resources and Where to Find Them</div>
</section>

<section class="slide col-l" style="top:1357px">
  <div class="s-head"><div class="t">Facts About HVMEF</div><div class="st">Number of Impact and BSTR Scholarships Awarded 2018-2019</div></div>
  <svg class="chart" style="left:40px;top:78px" width="420" height="180" viewBox="0 0 420 180" font-family="Lato, sans-serif">
    <g stroke="#e3e3e3"><line x1="60" y1="0" x2="60" y2="150"/><line x1="120" y1="0" x2="120" y2="150"/><line x1="180" y1="0" x2="180" y2="150"/><line x1="240" y1="0" x2="240" y2="150"/><line x1="300" y1="0" x2="300" y2="150"/><line x1="360" y1="0" x2="360" y2="150"/></g>
    <line x1="0" y1="150" x2="420" y2="150" stroke="#bbb"/>
    <g fill="#1a8fcf">
      <rect x="22" y="10" width="8" height="140"/><rect x="82" y="62" width="8" height="88"/><rect x="142" y="112" width="8" height="38"/>
      <rect x="202" y="100" width="8" height="50"/><rect x="262" y="92" width="8" height="58"/><rect x="322" y="8" width="8" height="142"/>
    </g>
    <g fill="#e2203c">
      <rect x="33" y="84" width="8" height="66"/><rect x="93" y="46" width="8" height="104"/><rect x="153" y="147" width="8" height="3"/>
      <rect x="213" y="70" width="8" height="80"/><rect x="273" y="122" width="8" height="28"/><rect x="333" y="64" width="8" height="86"/>
    </g>
    <g font-size="4.5" fill="#777" text-anchor="middle">
      <text x="31" y="160">DISTRICT I</text><text x="91" y="160">DISTRICT II</text><text x="151" y="160">DISTRICT III</text>
      <text x="211" y="160">DISTRICT IV</text><text x="271" y="160">DISTRICT V</text><text x="331" y="160">DISTRICT VI</text>
    </g>
    <g font-size="4.5" fill="#777"><rect x="158" y="170" width="4" height="4" fill="#1a8fcf"/><text x="164" y="174">Impact Scholarships</text><rect x="212" y="170" width="4" height="4" fill="#e2203c"/><text x="218" y="174">BSTR Scholarships</text></g>
  </svg>
  <span class="mark"></span>
</section>

<section class="slide col-r" style="top:1357px">
  <div class="s-head"><div class="t">Facts About HVMEF</div><div class="st">Sources of Contribution to the Fund</div></div>
  <svg class="chart" style="left:0;top:70px" width="487" height="200" viewBox="0 0 487 200" font-family="Lato, sans-serif">
    <text x="72" y="110" font-size="8" text-anchor="middle" fill="#333"><tspan x="72">The majority of</tspan><tspan x="72" dy="11">contributions made</tspan><tspan x="72" dy="11">are to fund Impact</tspan><tspan x="72" dy="11">Scholarships</tspan></text>
    <path d="M68 92 V70 H118" fill="none" stroke="#e2203c" stroke-width="5"/>
    <path d="M116 62 L128 70 L116 78 Z" fill="#e2203c"/>
    <g transform="rotate(-90 202 82)" fill="none" stroke-width="9">
      <circle cx="202" cy="82" r="68" stroke="#e2203c" stroke-dasharray="226 428"/>
      <circle cx="202" cy="82" r="68" stroke="#1a8fcf" stroke-dasharray="0 226 150 428"/>
      <circle cx="202" cy="82" r="68" stroke="#7b3fa8" stroke-dasharray="0 376 22 428"/>
      <circle cx="202" cy="82" r="68" stroke="#f29be8" stroke-dasharray="0 398 14 428"/>
      <circle cx="202" cy="82" r="68" stroke="#52ba9c" stroke-dasharray="0 412 5 428"/>
      <circle cx="202" cy="82" r="68" stroke="#f0a030" stroke-dasharray="0 417 6 428"/>
      <circle cx="202" cy="82" r="68" stroke="#c8177a" stroke-dasharray="0 423 5 428"/>
    </g>
    <text x="202" y="80" font-size="10" text-anchor="middle" fill="#222">Total Contributions</text>
    <text x="202" y="94" font-size="10" font-weight="700" text-anchor="middle" fill="#e2203c">$240,651.12</text>
    <g font-size="5.5" fill="#555">
      <rect x="308" y="15" width="6" height="6" fill="#d8e6c3"/><text x="318" y="20">Shop Rewards Program</text>
      <rect x="308" y="28" width="6" height="6" fill="#8fd0cc"/><text x="318" y="33">Ambassador Funded Scholarship</text>
      <rect x="308" y="41" width="6" height="6" fill="#3aa84a"/><text x="318" y="46">Edna Ross Scholarship</text>
      <rect x="308" y="54" width="6" height="6" fill="#f0a030"/><text x="318" y="59">Mae Collins Scholarship</text>
      <rect x="308" y="67" width="6" height="6" fill="#f06a40"/><text x="318" y="72">Board of Trustees Spring Conference Collections</text>
      <rect x="308" y="80" width="6" height="6" fill="#7b3fa8"/><text x="318" y="85">BSTR Contributions</text>
      <rect x="308" y="93" width="6" height="6" fill="#e8e03a"/><text x="318" y="98">Outright Grant Contributions</text>
      <rect x="308" y="106" width="6" height="6" fill="#1a8fcf"/><text x="318" y="111">General</text>
      <rect x="308" y="119" width="6" height="6" fill="#c3b6e0"/><text x="318" y="124">Annual Giving Day Event</text>
      <rect x="308" y="132" width="6" height="6" fill="#e2203c"/><text x="318" y="137">Impact Scholarship Contributions</text>
      <rect x="308" y="145" width="6" height="6" fill="#c8177a"/><text x="318" y="150">Grace Holt National Scholarship</text>
      <rect x="308" y="158" width="6" height="6" fill="#222"/><text x="318" y="163">Lena Ford National Scholarship</text>
      <rect x="308" y="171" width="6" height="6" fill="#f4b98a"/><text x="318" y="176">Member Pledges</text>
    </g>
  </svg>
  <span class="mark"></span>
</section>

<section class="slide col-l" style="top:1683px">
  <div class="s-head"><div class="t">Facts About HVMEF</div><div class="st">Impact and BSTR Disbursements by District 2018-2019</div></div>
  <svg class="chart" style="left:24px;top:70px" width="440" height="190" viewBox="0 0 440 190" font-family="Lato, sans-serif">
    <g font-size="5" fill="#888" text-anchor="end">
      <text x="36" y="25">$12,000.00</text><text x="36" y="46">$10,000.00</text><text x="36" y="67">$8,000.00</text><text x="36" y="88">$6,000.00</text><text x="36" y="109">$4,000.00</text><text x="36" y="130">$2,000.00</text><text x="36" y="151">$0.00</text>
    </g>
    <rect x="129" y="31" width="50" height="118" fill="#1a8fcf"/>
    <rect x="207" y="139" width="50" height="10" fill="#e2203c"/>
    <rect x="288" y="38" width="50" height="111" fill="#1a8fcf"/>
    <g font-size="5" fill="#666"><text x="186" y="57">$11,200.00</text><text x="218" y="124">$1,000.00</text><text x="350" y="75">$10,600.00</text><text x="78" y="142">$0.00</text></g>
    <g stroke="#999" stroke-width=".5"><line x1="179" y1="40" x2="186" y2="54"/><line x1="232" y1="127" x2="232" y2="139"/><line x1="338" y1="45" x2="350" y2="72"/><line x1="86" y1="144" x2="129" y2="149"/></g>
    <g font-size="5" fill="#888" text-anchor="middle"><text x="154" y="160">District III</text><text x="313" y="160">District V</text></g>
    <g font-size="5" fill="#888"><rect x="190" y="170" width="4" height="4" fill="#e2203c"/><text x="196" y="174">BSTR</text><rect x="212" y="170" width="4" height="4" fill="#1a8fcf"/><text x="218" y="174">Impact</text></g>
  </svg>
  <span class="mark"></span>
</section>

<section class="slide survey col-r" style="top:1683px">
  <div class="frame"></div>
  <h3>Quick Survey</h3>
  <div class="rule"></div>
  <div class="q">?</div>
  <ol>
    <li>In 2019, the average annual earnings for women without a college education were:
      <ul><li>A.&nbsp; $28K</li><li>B.&nbsp; $36K</li><li>C.&nbsp; $41K</li></ul></li>
    <li>In 2019, women with at least a bachelor's (or greater) earned:
      <ul><li>A.&nbsp; $20K more</li><li>B.&nbsp; $15K more</li><li>C.&nbsp; $10K more</li></ul></li>
    <li>The average cost of one year of instate tuition for a public school (college/university) is:
      <ul><li>A.&nbsp; $15K</li><li>B.&nbsp; $20K</li><li>C.&nbsp; $25K</li></ul></li>
  </ol>
  <span class="mark" style="background:#fff"></span>
</section>

<section class="slide col-l" style="top:2013px">
  <div class="s-head"><div class="t">Facts About HVMEF</div><div class="st">Scholarships Awarded in 2018-2019</div></div>
  <div class="covers">
    <div class="img" role="img" aria-label="Magazine covers featuring scholarship recipients"></div>
    <p>Scholarships awarded are generally listed in the fall issue of Women at Work Magazine®</p>
    <small>Cover images shown courtesy of the publisher</small>
  </div>
  <div class="stats">
    <div><strong><em>4</em> ($17,500)</strong>National Scholarships Awarded</div>
    <div><strong><em>52</em> ($89,000)</strong>Impact Scholarships Awarded</div>
    <div><strong><em>38</em> ($3,772)</strong>BSTR Scholarships Awarded</div>
  </div>
  <span class="mark"></span>
</section>

<section class="slide mission col-r" style="top:2013px">
  <div class="img" role="img" aria-label="Photo of a graduate in cap and gown overlooking a city at dusk"></div>
  <h3>HVMEF'S MISSION<br>STATEMENT</h3>
  <p>The Harriet Vale Memorial Education Fund exists to provide educational grants and scholarships to women pursuing post secondary educational goals as well as ongoing professional development in order to support their career advancement and to help them become the role models, mentors and leaders of the future.</p>
  <span class="mark"></span>
</section>

<section class="slide facts col-l" style="top:2348px">
  <div class="s-head"><div class="t">Facts About HVMEF</div></div>
  <ul>
    <li>In 1953, HVMEF was established by Ruth Danner (the first honorary member of AWBN) in memory of Harriet Vale, a daughter of AWBN's founder, Mr. Arthur Vale Jr.</li>
    <li>HVMEF is a public foundation and is classified as a 501c3, a charitable organization.</li>
    <li class="sub">Because HVMEF is a charitable organization, all contributions to the fund are tax-exempt.</li>
    <li>Trustees award about $120,000 in scholarships annually.</li>
  </ul>
  <div class="img" role="img" aria-label="Photo of a graduate walking toward a campus building"></div>
  <span class="mark"></span>
</section>

<section class="slide bstr col-r" style="top:2348px">
  <h3>HVMEF - Business Skills Tuition Reimbursement (BSTR)</h3>
  <h4>Overview</h4>
  <ul>
    <li>As of 2020-2021, <b>70%</b> of the funds contributed are available for a league to offer a member/non-member a BSTR.</li>
    <li>A league may sponsor multiple BSTRs each year.</li>
    <li>The minimum amount of any BSTR scholarship is $50 and the maximum amount awarded to a single applicant in a given Award Year is $500.</li>
    <li>A BSTR is intended to be used for fees associated with professional development (non-degree) including licenses. For example, CPA or real estate would be covered as long as the other criteria is met (i.e., female, completion and payment of the course in advance of application, and the credentialing organization must meet the qualification).</li>
    <li>Prime Courses do not qualify for BSTR however, State U classes do.</li>
  </ul>
  <div class="img" role="img" aria-label="Photo of an audience raising hands at a conference"></div>
  <span class="mark"></span>
</section>

<section class="slide natl col-l" style="top:2675px">
  <h3>National Scholarship</h3>
  <div class="card">
    <div class="img" role="img" aria-label="Portrait photo of the scholarship's namesake"></div>
    <div class="rule"></div>
    <h4>Marion Keller Friendship<br>Scholarship</h4>
    <ul>
      <li><b>Scholarship Value:</b> $5,000</li>
      <li><b>Field of Study:</b> Business</li>
      <li><b>GPA:</b> 3.0 or higher</li>
      <li><b>Institution:</b> University or College in the state of Texas</li>
      <li><b>Level:</b> Freshman to Graduate</li>
    </ul>
  </div>
  <span class="mark"></span>
</section>

<section class="slide thanks col-r" style="top:2675px">
  <h3>Thanks for Attending<br>Today's HVMEF Session!</h3>
  <div class="person" style="left:40px"><div class="img" role="img" aria-label="Portrait photo of Joan Palmer"></div><div class="nm">Joan Palmer</div><div class="rl">National Secretary-Treasurer</div></div>
  <div class="person" style="left:179px"><div class="img" role="img" aria-label="Portrait photo of Linda Morrow"></div><div class="nm">Linda Morrow</div><div class="rl">District III Vice President</div></div>
  <div class="person" style="left:318px"><div class="img" role="img" aria-label="Portrait photo of Paula Grant"></div><div class="nm">Paula Grant</div><div class="rl">District V Vice President</div></div>
  <div class="footbar"></div>
</section>

</body>
</html>
```